Brackwell Immigration Law

We need a web design for our existing company www.brackwellcounsel.co.uk. We are an immigration consultancy. The final design should communicate professionalism, integrity and affordability.

Industry/Entity Type

It Company

Logo Text

Brackwell Counsel Partners

Number of Pages Required

5+ page

Font styles to use
Serif

Requirements
Must have
• I want to have the same silhouette logo but something different in positioning..
Nice to have
• Please have a look at these websites:
• https://www.travelpathguide.co.uk/visa_uk/
• http://www.oakdenadvisers.co.uk/
• http://www.myrtlegatelaw.org/index.php
• www.brackwellcounsel.co.uk

```html
<!DOCTYPE html>
<html lang="en">
<head>
<meta charset="utf-8">
<title>Brackwell Counsel Partners – Immigration Law</title>
<link href="https://fonts.googleapis.com/css2?family=Playfair+Display:wght@400;700&family=Open+Sans:wght@400;600;700&display=swap" rel="stylesheet">
<style>
:root{
  --green:#3f5f2b;
  --green-dark:#2f4a1f;
  --ink:#2a2a2a;
  --muted:#777;
  --line:#d9d9d9;
  --paper:#ffffff;
  --soft:#f2f2f0;
  --footer:#2c2c2c;
  --footer-deep:#1e1e1e;
  --icon:#3a3a3a;
}
*{box-sizing:border-box;margin:0;padding:0}
html,body{width:831px;height:1200px;overflow:hidden}
body{font-family:"Open Sans",Arial,sans-serif;color:var(--ink);background:var(--paper);position:relative;font-size:10px}
.serif{font-family:"Playfair Display",Georgia,serif}

/* header */
.site-header{position:absolute;top:0;left:0;width:831px;height:80px;background:var(--paper);border-bottom:1px solid var(--line)}
.brand{position:absolute;left:22px;top:18px;display:flex;align-items:center;gap:8px}
.brand-mark{width:30px;height:30px;background:var(--ink);border-radius:50%}
.brand-name{font-family:"Playfair Display",Georgia,serif;font-size:14px;font-weight:700;color:var(--ink);line-height:1.1;width:110px}
.main-nav{position:absolute;left:218px;top:44px;display:flex}
.main-nav a{display:block;padding:0 10px;height:22px;line-height:22px;font-size:9px;font-weight:600;color:var(--ink);text-decoration:none;border-right:1px solid var(--line)}
.main-nav a:last-child{border-right:none}
.main-nav a.active{color:var(--green)}
.call-box{position:absolute;right:22px;top:10px;text-align:right}
.call-box .label{font-size:9px;color:var(--muted)}
.call-box .phone{font-size:13px;font-weight:700;color:var(--ink)}
.btn-callback{position:absolute;right:22px;top:44px;background:var(--green);color:#fff;font-size:8.5px;font-weight:700;padding:6px 10px;letter-spacing:.3px}

/* hero */
.hero{position:absolute;top:80px;left:0;width:831px;height:245px;background:linear-gradient(180deg,#8fa6b8 0%,#c9d3d8 55%,#a7a39a 100%)}
.hero-title{position:absolute;left:58px;top:62px;font-family:"Playfair Display",Georgia,serif;color:#fff;font-size:30px;line-height:1.2;text-shadow:0 1px 3px rgba(0,0,0,.35)}
.hero-title .sub{font-size:26px}
.flag{display:inline-block;width:26px;height:17px;background:#3b4e8c;vertical-align:middle;margin-left:6px}
.hero-arrow{position:absolute;top:100px;width:26px;height:40px;background:rgba(0,0,0,.45);display:flex;align-items:center;justify-content:center}
.hero-arrow.left{left:0}.hero-arrow.right{right:0}

/* services */
.services{position:absolute;top:325px;left:0;width:831px;height:165px;background:var(--soft);display:flex;justify-content:space-around;padding:22px 20px 0}
.service{width:110px;text-align:center}
.service-ring{width:84px;height:84px;border-radius:50%;border:5px solid #e0e0dc;background:#fff;margin:0 auto;display:flex;align-items:center;justify-content:center;box-shadow:0 1px 3px rgba(0,0,0,.15)}
.service-ring .core{width:62px;height:62px;border-radius:50%;background:var(--icon);display:flex;align-items:center;justify-content:center}
.service p{margin-top:10px;font-size:9px;line-height:1.3;color:var(--ink)}

/* about */
.about{position:absolute;top:490px;left:0;width:831px;height:245px;background:linear-gradient(135deg,#4a4a48,#2e2f2d 60%,#3c3b38)}
.about-title{position:absolute;left:50%;transform:translateX(-50%);top:26px;border:1px solid rgba(255,255,255,.7);color:#fff;padding:7px 20px;font-family:"Playfair Display",Georgia,serif;font-size:15px;white-space:nowrap}
.about-text{position:absolute;left:70px;top:78px;width:690px;color:#e6e6e6;font-size:10px;line-height:1.7;text-align:center}
.read-more{position:absolute;left:50%;transform:translateX(-50%);top:170px;color:#fff;font-size:10px;font-weight:700}

/* columns */
.columns{position:absolute;top:735px;left:0;width:831px;height:255px;background:#fff;display:flex;padding:14px 22px 0;gap:22px}
.col h3{font-family:"Playfair Display",Georgia,serif;font-size:12px;font-weight:700;color:var(--ink);text-transform:uppercase}
.col .kicker{font-size:8px;color:var(--muted);margin-bottom:10px}
.col-head{display:flex;justify-content:space-between;align-items:flex-start;border-bottom:1px solid var(--line);margin-bottom:10px}
.enquiry{width:255px}
.form-row{display:flex;gap:10px;margin-bottom:8px}
.field{flex:1}
.field label{font-size:8px;color:var(--muted);display:block;margin-bottom:2px}
.field .box{height:16px;border:1px solid var(--line)}
.field .area{height:50px;border:1px solid var(--line)}
.submit{margin-left:auto;display:block;width:54px;background:var(--green);color:#fff;font-size:9px;font-weight:700;text-align:center;padding:5px 0}
.reviews{width:270px}
.pager{display:flex;gap:3px}
.pager span{width:16px;height:16px;background:var(--ink);display:flex;align-items:center;justify-content:center}
.pager span.on{background:var(--green)}
.quote{font-size:9px;line-height:1.6;color:#555;font-style:italic;padding:4px 4px 0 14px;position:relative}
.quote:before{content:"\201C";position:absolute;left:0;top:-4px;font-size:22px;color:var(--green);font-family:"Playfair Display",Georgia,serif}
.reviewer{display:flex;align-items:center;gap:10px;margin-top:18px;padding-left:50px}
.avatar{width:38px;height:38px;border-radius:50%;background:#9a9893}
.reviewer strong{font-size:10px}
.news{flex:1}
.news-item{display:flex;gap:8px;margin-bottom:8px}
.date{width:30px;background:var(--green);color:#fff;text-align:center;flex:none}
.date b{display:block;font-size:12px;line-height:16px}
.date small{display:block;font-size:7px;background:var(--green-dark);line-height:10px}
.news-item p{font-size:8px;line-height:1.35;color:#555}
.news-item p b{color:var(--ink);display:block}

/* cta row */
.cta-row{position:absolute;top:990px;left:0;width:831px;height:60px;display:flex;gap:12px;padding:8px 22px;background:#fff}
.cta{flex:1;height:40px;border-radius:6px;display:flex;align-items:center;gap:10px;padding:0 14px;font-family:"Playfair Display",Georgia,serif;font-size:11px;font-weight:700;border:1px solid var(--line);color:var(--ink)}
.cta.dark{background:var(--green);color:#fff;border-color:var(--green)}
.cta .ico{width:26px;height:26px;border-radius:50%;background:var(--icon);display:flex;align-items:center;justify-content:center;flex:none}
.cta.dark .ico{background:#fff}

/* footer */
.site-footer{position:absolute;top:1050px;left:0;width:831px;height:128px;background:var(--footer);color:#ccc;display:flex;gap:30px;padding:12px 22px}
.site-footer h4{font-size:9px;color:#fff;text-transform:uppercase;border-bottom:1px solid #555;padding-bottom:4px;margin-bottom:6px;font-weight:700}
.quick-links{width:150px}
.quick-links li{list-style:none;font-size:8px;line-height:12.5px}
.quick-links li:before{content:"› ";color:#8fb069}
.location{width:190px}
.map{width:190px;height:82px;background:linear-gradient(135deg,#9fb8cf,#c8d6c0 60%,#b6c7d8)}
.contact{width:180px;font-size:8px;line-height:13px}
.contact b{color:#fff;font-weight:600}
.footer-brand{flex:1;display:flex;align-items:center;gap:8px;justify-content:flex-end}
.footer-brand .brand-mark{background:#fff}
.footer-brand .brand-name{color:#fff}
.bottom-bar{position:absolute;top:1178px;left:0;width:831px;height:22px;background:var(--green-dark);color:#e8e8e8;font-size:8px;display:flex;align-items:center;justify-content:space-between;padding:0 22px}
.social{display:flex;gap:4px}
.social span{width:12px;height:12px;background:rgba(255,255,255,.8)}
</style>
</head>
<body>

<header class="site-header">
  <div class="brand"><span class="brand-mark"></span><span class="brand-name">Brackwell Counsel Partners</span></div>
  <nav class="main-nav">
    <a href="#" class="active">HOME</a><a href="#">ABOUT US</a><a href="#">SERVICES</a><a href="#">NEWS</a><a href="#">TESTIMONIALS</a><a href="#">CONTACT US</a>
  </nav>
  <div class="call-box"><div class="label">Call us today</div><div class="phone">123-456-7890</div></div>
  <div class="btn-callback">REQUEST A CALL BACK</div>
</header>

<section class="hero" role="img" aria-label="Photo of a person with a laptop sitting on a ledge under a cloudy sky with a hot air balloon">
  <h1 class="hero-title">We Bring Your Dreams<br>Come True <span class="flag" role="img" aria-label="United Kingdom flag"></span><br><span class="sub">To Work &amp; Stay In Uk</span></h1>
  <div class="hero-arrow left"><svg width="10" height="14" viewBox="0 0 10 14"><path d="M8 1 2 7l6 6" fill="none" stroke="#fff" stroke-width="2"/></svg></div>
  <div class="hero-arrow right"><svg width="10" height="14" viewBox="0 0 10 14"><path d="M2 1l6 6-6 6" fill="none" stroke="#fff" stroke-width="2"/></svg></div>
</section>

<section class="services">
  <div class="service"><div class="service-ring"><div class="core"><svg width="32" height="22" viewBox="0 0 32 22"><circle cx="11" cy="11" r="8" fill="none" stroke="#fff" stroke-width="2.5"/><circle cx="21" cy="11" r="8" fill="none" stroke="#fff" stroke-width="2.5"/></svg></div></div><p>Marriage, Fiance,<br>Relationship Visas</p></div>
  <div class="service"><div class="service-ring"><div class="core"><svg width="30" height="24" viewBox="0 0 30 24"><rect x="2" y="6" width="26" height="16" rx="2" fill="#fff"/><rect x="10" y="2" width="10" height="6" fill="none" stroke="#fff" stroke-width="2"/></svg></div></div><p>Work Visa</p></div>
  <div class="service"><div class="service-ring"><div class="core"><svg width="30" height="26" viewBox="0 0 30 26"><circle cx="10" cy="7" r="5" fill="#fff"/><circle cx="21" cy="9" r="4" fill="#fff"/><path d="M1 25c0-7 4-10 9-10s9 3 9 10zM16 25c0-5 2-8 5-8s7 2 7 8z" fill="#fff"/></svg></div></div><p>Adult Dependent<br>Relative Visas</p></div>
  <div class="service"><div class="service-ring"><div class="core"><svg width="30" height="30" viewBox="0 0 30 30"><path d="M3 17l24-10-6 18-6-7z" fill="#fff"/></svg></div></div><p>Visiting Visa</p></div>
  <div class="service"><div class="service-ring"><div class="core"><svg width="30" height="26" viewBox="0 0 30 26"><path d="M15 2 2 13h4v11h18V13h4z" fill="#fff"/></svg></div></div><p>Indefinite To<br>Remain</p></div>
  <div class="service"><div class="service-ring"><div class="core"><svg width="26" height="30" viewBox="0 0 26 30"><path d="M13 2 2 6v8c0 7 5 12 11 14 6-2 11-7 11-14V6z" fill="#fff"/><path d="M8 15l4 4 7-8" fill="none" stroke="#3a3a3a" stroke-width="2.5"/></svg></div></div><p>British<br>Citizenship</p></div>
</section>

<section class="about" role="img" aria-label="Dark toned photo of a city skyline behind the about section">
  <h2 class="about-title">About Brackwell Counsel Partners</h2>
  <p class="about-text">We are a team of registered immigration advisers helping families, workers and students settle in the United Kingdom. From first consultation to final decision, we prepare every application with care, explain each step in plain language and keep our fees clear and fair. Our advisers have guided thousands of clients through visas, extensions and citizenship, and we stay beside you until your future here is secure.</p>
  <span class="read-more">Read More</span>
</section>

<section class="columns">
  <div class="col enquiry">
    <div class="col-head"><div><h3>Quick Enquiry</h3><div class="kicker">Write to us</div></div></div>
    <div class="form-row"><div class="field"><label>First Name*</label><div class="box"></div></div><div class="field"><label>Last Name*</label><div class="box"></div></div></div>
    <div class="form-row"><div class="field"><label>Phone*</label><div class="box"></div></div><div class="field"><label>Email*</label><div class="box"></div></div></div>
    <div class="form-row"><div class="field"><label>Description of a problem*</label><div class="area"></div></div></div>
    <span class="submit">Submit</span>
  </div>
  <div class="col reviews">
    <div class="col-head"><div><h3>Customer Reviews</h3><div class="kicker">What other said about us</div></div>
      <div class="pager"><span><svg width="6" height="8" viewBox="0 0 6 8"><path d="M5 0 0 4l5 4z" fill="#fff"/></svg></span><span class="on"><svg width="6" height="8" viewBox="0 0 6 8"><path d="M1 0l5 4-5 4z" fill="#fff"/></svg></span></div></div>
    <p class="quote">Professional, patient and always honest. They explained every document I needed, kept me updated each week and my visa was approved first time. I recommend them to anyone starting the process.</p>
    <div class="reviewer"><span class="avatar" role="img" aria-label="Client portrait"></span><strong>Mr Daniel Harlow</strong></div>
  </div>
  <div class="col news">
    <div class="col-head"><div><h3>Latest News</h3><div class="kicker">Latest happening</div></div></div>
    <div class="news-item"><div class="date"><b>26</b><small>DEC</small></div><p><b>New visa rules announced</b>Changes take effect this spring</p></div>
    <div class="news-item"><div class="date"><b>25</b><small>DEC</small></div><p><b>Family route fees updated</b>Check the new costs here</p></div>
    <div class="news-item"><div class="date"><b>24</b><small>DEC</small></div><p><b>Skilled worker list revised</b>More roles now qualify today</p></div>
    <div class="news-item"><div class="date"><b>23</b><small>DEC</small></div><p><b>Citizenship test dates open</b>Book your place early now</p></div>
  </div>
</section>

<section class="cta-row">
  <div class="cta"><span class="ico"><svg width="14" height="14" viewBox="0 0 14 14"><circle cx="7" cy="7" r="6" fill="none" stroke="#fff" stroke-width="1.5"/><path d="M7 3v4h3" fill="none" stroke="#fff" stroke-width="1.5"/></svg></span>Same Day Service</div>
  <div class="cta dark"><span class="ico"><svg width="14" height="14" viewBox="0 0 14 14"><rect x="1" y="3" width="12" height="10" fill="none" stroke="#3a3a3a" stroke-width="1.5"/><path d="M1 6h12M4 1v3M10 1v3" stroke="#3a3a3a" stroke-width="1.5"/></svg></span>Weekend Service</div>
  <div class="cta"><span class="ico"><svg width="14" height="12" viewBox="0 0 14 12"><rect x="1" y="1" width="12" height="10" fill="none" stroke="#fff" stroke-width="1.5"/><path d="M1 1l6 5 6-5" fill="none" stroke="#fff" stroke-width="1.5"/></svg></span>Sign up For Newsletter</div>
  <div class="cta dark"><span class="ico"><svg width="14" height="14" viewBox="0 0 14 14"><path d="M7 1v8M3 6l4 4 4-4M2 13h10" fill="none" stroke="#3a3a3a" stroke-width="1.6"/></svg></span>Download Our Brochure</div>
</section>

<footer class="site-footer">
  <div class="quick-links"><h4>Quick Links</h4><ul><li>Home</li><li>About Us</li><li>Services</li><li>News</li><li>Policy</li><li>Testimonials</li><li>Contact Us</li></ul></div>
  <div class="location"><h4>Our Location</h4><div class="map" role="img" aria-label="Map of the office location in the United Kingdom"></div></div>
  <div class="contact"><h4>Contact Details</h4><b>Phone</b><br>123-456-7890<br><b>Address</b><br>14 Kestrel Row, London<br><b>Email</b> info@brackwellcounsel.co.uk<br>Monday to Friday 9am–6pm</div>
  <div class="footer-brand"><span class="brand-mark"></span><span class="brand-name">Brackwell Counsel Partners</span></div>
</footer>
<div class="bottom-bar"><span>Copyright 2014 Brackwell Counsel Partners. All Rights Reserved</span><span class="social"><span></span><span></span><span></span><span></span></span></div>

</body>
</html>
```